Business Cards for Corvantis LLC

We need business cards for a new company called “Corvantis LLC”. This is a technology process improvement company providing a comprehensive assessment of the technology used to run their business. The documentation and review process delivers the visibility and reassurance they need to protect their business and plan for the future. The product is called “Halvorne Ledgerwork”. Our primary target is small-medium size businesses, with the deliverables going to the decision maker. We would like to see the designs use the color blue. Our tag line is PROTECT YOUR BUSINESS · TAKE CONTROL OF IT.

Industry/Entity Type

Business

Contact Information for Business Card

Tag line should be on back of card - it does not have to be upper case.

Requirements
Must have
• Please use information when laying out card:
• Name: Darnell Pruitt
• Title: Partner
• Phone Number: (877)555-0143
• Email: dell@corvantisllc.com
• Website: http://corvantisllc.com

```html
<!DOCTYPE html>
<html lang="en">
<head>
<meta charset="utf-8">
<title>Corvantis LLC — Business Cards</title>
<link rel="stylesheet" href="https://fonts.googleapis.com/css2?family=Exo+2:ital,wght@0,400;0,600;0,700;1,400&family=Open+Sans:wght@400&display=swap">
<style>
  :root {
    --brand-blue: #0f76bd;
    --band-grey: #7f8285;
    --ink-grey: #4a4d50;
    --paper: #ffffff;
    --backdrop: #e9e7e4;
  }
  * { margin: 0; padding: 0; box-sizing: border-box; }
  html, body {
    width: 1200px;
    height: 987px;
    overflow: hidden;
    background: var(--backdrop);
  }
  .sheet { position: relative; width: 1200px; height: 987px; }

  .card {
    position: absolute;
    left: 293px;
    width: 615px;
    height: 350px;
    box-shadow: 0 2px 6px rgba(0,0,0,0.18);
  }
  .card--front { top: 130px; background: var(--paper); }
  .card--back { top: 506px; background: var(--brand-blue); }

  /* Front */
  .header-band {
    position: absolute;
    left: 0; right: 0;
    top: 26px;
    height: 80px;
    background: var(--brand-blue);
  }
  .header-band__grey {
    position: absolute;
    left: 0; top: 0; bottom: 0;
    width: 178px;
    background: var(--band-grey);
  }
  .person {
    position: absolute;
    right: 26px;
    top: 40px;
    text-align: right;
    color: var(--paper);
    font-family: "Exo 2", sans-serif;
  }
  .person__name { font-size: 21px; font-weight: 700; line-height: 1.1; }
  .person__title { font-size: 15px; font-weight: 400; margin-top: 4px; }

  .wordmark {
    position: absolute;
    font-family: "Exo 2", sans-serif;
    font-weight: 700;
    letter-spacing: 1px;
    white-space: nowrap;
  }
  .card--front .wordmark {
    left: 44px;
    top: 112px;
    font-size: 28px;
    color: var(--brand-blue);
  }

  .contact {
    position: absolute;
    left: 44px;
    top: 255px;
    list-style: none;
    font-family: "Exo 2", sans-serif;
    font-size: 15px;
    color: var(--ink-grey);
  }
  .contact li {
    display: flex;
    align-items: center;
    height: 23.5px;
  }
  .contact svg { width: 14px; height: 14px; margin-right: 9px; fill: var(--brand-blue); }

  .tagline--front {
    position: absolute;
    right: 35px;
    top: 277px;
    text-align: right;
    font-family: "Exo 2", sans-serif;
    font-style: italic;
    font-size: 17px;
    line-height: 23.5px;
    color: var(--ink-grey);
  }

  /* Back */
  .card--back .wordmark {
    left: 40px;
    top: 230px;
    width: 240px;
    text-align: center;
    font-size: 28px;
    color: var(--paper);
  }
  .tagline--back {
    position: absolute;
    left: 40px;
    top: 280px;
    width: 240px;
    text-align: center;
    font-family: "Open Sans", sans-serif;
    font-size: 16px;
    line-height: 23px;
    color: var(--paper);
  }
</style>
</head>
<body>
<main class="sheet">

  <section class="card card--front" aria-label="Business card front">
    <div class="header-band"><div class="header-band__grey"></div></div>
    <div class="person">
      <p class="person__name">Darnell Pruitt</p>
      <p class="person__title">Partner</p>
    </div>
    <p class="wordmark">Corvantis LLC</p>

    <ul class="contact">
      <li>
        <svg viewBox="0 0 24 24" aria-hidden="true"><path d="M6.6 10.8a15.1 15.1 0 0 0 6.6 6.6l2.2-2.2c.3-.3.7-.4 1-.2 1.1.4 2.3.6 3.6.6.6 0 1 .4 1 1V20c0 .6-.4 1-1 1A17 17 0 0 1 3 4c0-.6.4-1 1-1h3.5c.6 0 1 .4 1 1 0 1.3.2 2.5.6 3.6.1.3 0 .7-.2 1z"/></svg>
        (877)555-0143
      </li>
      <li>
        <svg viewBox="0 0 24 24" aria-hidden="true"><path d="M2 5h20v14H2z M2 5l10 8 10-8" /></svg>
        dell@corvantisllc.com
      </li>
      <li>
        <svg viewBox="0 0 24 24" aria-hidden="true"><circle cx="12" cy="12" r="10"/></svg>
        www.corvantisllc.com
      </li>
    </ul>

    <p class="tagline--front">Protect your business.<br>Take control of it.</p>
  </section>

  <section class="card card--back" aria-label="Business card back">
    <p class="wordmark">Corvantis LLC</p>
    <p class="tagline--back">Protect your business.<br>Take control of it.</p>
  </section>

</main>
</body>
</html>
```